36" inch (height) x 96" inch (width) Banner for Baseball Field

Hello. This project is an advertisement that will be printed onto a 3 foot by 8 foot full color banner and placed at little league fields in Southern California. A theme of the banner can be baseball. The company is my law office practicing Estate Planning and Tax Law. I am uploading the current business card, which has the logo, website, and telephone number. You can also pull images from www.rkpembrove.com I would like the banner to be a fun design that incorporates baseball somehow, but draws attention to my law and tax office, and my website. Please be creative, and have fun with it. The colors of my practice are included in the logo. At the bottom, it should say "Attorney Advertisement," but this can be in very small font in the bottom right or left corner.

Target Market(s)

Youth Baseball Fans

Industry/Entity Type

Law; Accounting

Colors

Designer to choose colors to be used in the design.

Requirements
Must have
• My telephone number. My website.
Nice to have
• Would like to see "Estate Planning" and "Tax Law and Preparation" Would also like to see "Attorney" and "CPA" or "Certified Public Accountant" prominently diplayed

```html
<!DOCTYPE html>
<html lang="en">
<head>
<meta charset="UTF-8">
<title>RK Pembrove Field Banner</title>
<link rel="stylesheet" href="https://fonts.googleapis.com/css2?family=Playfair+Display:wght@700;800&family=Oswald:wght@600&family=Montserrat:wght@600;700;800&family=Cinzel:wght@400;600&display=swap">
<style>
  :root {
    --ink: #0a0b0e;
    --brand-blue: #1e90d0;
    --white: #ffffff;
    --page: #ffffff;
    --photo-dark: #14171d;
    --photo-leather: #8a5a22;
    --photo-gold: #b08a3e;
  }
  html, body {
    margin: 0;
    width: 1100px;
    height: 1200px;
    overflow: hidden;
    background: var(--page);
  }
  .banner {
    position: absolute;
    left: 50px;
    top: 412px;
    width: 1000px;
    height: 375px;
    box-shadow: 0 4px 14px rgba(0,0,0,0.25);
  }
  .banner svg { display: block; }
  .headline { font-family: "Playfair Display", Georgia, serif; font-weight: 800; }
  .subhead { font-family: "Playfair Display", Georgia, serif; font-weight: 700; }
  .band-text { font-family: "Oswald", "Arial Narrow", sans-serif; font-weight: 600; }
  .contact { font-family: "Montserrat", Arial, sans-serif; font-weight: 700; }
  .firm { font-family: "Cinzel", Georgia, serif; }
</style>
</head>
<body>
  <div class="banner">
    <svg width="1000" height="375" viewBox="0 0 1000 375" xmlns="http://www.w3.org/2000/svg">
      <defs>
        <linearGradient id="photoFade" x1="0" y1="0" x2="1" y2="0">
          <stop offset="0" stop-color="#0a0b0e" stop-opacity="0"/>
          <stop offset="0.35" stop-color="#14171d"/>
          <stop offset="1" stop-color="#1a1c22"/>
        </linearGradient>
        <radialGradient id="photoTones" cx="0.6" cy="0.65" r="0.55">
          <stop offset="0" stop-color="#b08a3e" stop-opacity="0.75"/>
          <stop offset="0.45" stop-color="#8a5a22" stop-opacity="0.55"/>
          <stop offset="1" stop-color="#14171d" stop-opacity="0"/>
        </radialGradient>
      </defs>

      <rect class="banner-bg" width="1000" height="375" fill="var(--ink)"/>

      <g class="hero-photo" role="img" aria-label="Photo of a baseball glove, ball and bat in front of golden scales of justice on a dark backdrop">
        <rect x="560" y="0" width="440" height="375" fill="url(#photoFade)"/>
        <rect x="560" y="0" width="440" height="375" fill="url(#photoTones)"/>
      </g>

      <text class="headline" x="26" y="85" font-size="82" fill="var(--brand-blue)" textLength="716" lengthAdjust="spacingAndGlyphs">ESTATE PLANNING</text>
      <text class="subhead" x="30" y="135" font-size="56" fill="var(--white)" textLength="707" lengthAdjust="spacingAndGlyphs">&amp; TAX LAW PREPERATION</text>

      <path class="accent-band" d="M0 155 H690 Q712 155 722 175 L716 223 H0 Z" fill="var(--brand-blue)"/>
      <text class="band-text" x="28" y="212" font-size="60" fill="var(--white)" textLength="632" lengthAdjust="spacingAndGlyphs">CERTIFIED PUBLIC ACCOUNTANT</text>

      <g class="firm-name">
        <circle cx="118" cy="266" r="26" fill="none" stroke="var(--brand-blue)" stroke-width="4"/>
        <text class="firm" x="118" y="307" font-size="10.5" fill="var(--white)" text-anchor="middle" letter-spacing="0.5">THE LAW OFFICES OF</text>
        <text class="firm" x="118" y="334" font-size="22" fill="var(--brand-blue)" text-anchor="middle" textLength="188" lengthAdjust="spacingAndGlyphs">RK PEMBROVE</text>
      </g>

      <g class="contact-block">
        <text class="contact" x="233" y="258" font-size="18" fill="var(--white)" textLength="198" lengthAdjust="spacingAndGlyphs">CONTACT US NOW!</text>
        <circle cx="249" cy="292" r="16" fill="var(--brand-blue)"/>
        <path d="M242 284 q-2 3 1 9 q4 7 10 9 q3 1 5-1 l-3-4 q-2 1-3 0 q-4-3-5-7 q0-2 1-2 l-3-4z" fill="var(--ink)"/>
        <text class="contact" x="270" y="305" font-size="37" fill="var(--white)" textLength="278" lengthAdjust="spacingAndGlyphs">(805) 555-0142</text>
        <text class="contact" x="233" y="340" font-size="24" fill="var(--white)" textLength="358" lengthAdjust="spacingAndGlyphs">www.<tspan fill="var(--brand-blue)">RKPEMBROVE</tspan>.com</text>
      </g>

      <path class="disclaimer-tab" d="M748 338 H1000 V375 H732 Q738 342 748 338 Z" fill="var(--brand-blue)"/>
      <text class="contact" x="866" y="362" font-size="13.5" font-weight="600" fill="var(--white)" text-anchor="middle" letter-spacing="0.4">ATTORNEY ADVERTISEMENT</text>
    </svg>
  </div>
</body>
</html>
```